Brochure Design Project

Create a design for parent and family education program (using attached text) that can serve as a template for other brochures

Industry/Entity Type

Education

Requirements
Must have
• leave space for one logo (same logo as on attached)

```html
<!DOCTYPE html>
<html lang="en">
<head>
<meta charset="utf-8">
<title>Oh Baby! – Saint Amory's Family Education</title>
<link rel="stylesheet" href="https://fonts.googleapis.com/css2?family=Arimo:ital,wght@0,400;0,700;1,400&display=swap">
<style>
  :root{
    --green:#8cc63f;
    --blue:#3b82c4;
    --blue-deep:#1f6fb8;
    --ink:#1a1a1a;
    --white:#ffffff;
    --photo-warm:#e9d8cf;
    --photo-skin:#d9b8a4;
    --photo-coat:#eef1f4;
  }
  *{margin:0;padding:0;box-sizing:border-box}
  html,body{width:1200px;height:776px;overflow:hidden;background:var(--white)}
  .brochure{position:relative;width:1200px;height:776px;overflow:hidden;font-family:"Arimo",Arial,sans-serif;color:var(--ink);background:var(--white)}
  .waves{position:absolute;left:0;top:0;width:1200px;height:776px}
  .photo{position:absolute}
  .photo--crawling-baby{left:360px;top:4px;width:175px;height:205px;border-radius:45% 40% 50% 45%;background:radial-gradient(circle at 50% 40%,var(--photo-skin),#cfe0ee 75%,rgba(255,255,255,0) 76%)}
  .photo--mother-baby{left:266px;top:420px;width:326px;height:282px;background:linear-gradient(160deg,#f6eee9,var(--photo-warm) 55%,#cbb2a3)}
  .photo--clinician{left:1010px;top:385px;width:190px;height:391px;background:linear-gradient(180deg,#c9a58f 0%,#e7dcd5 30%,var(--photo-coat) 45%,#dfe4ea 100%);border-radius:80px 80px 0 0}
  .block{position:absolute}
  .block h2{font-weight:400;color:var(--blue);font-size:20px;line-height:24px;margin-bottom:8px}
  .block p{font-size:12px;line-height:14.2px}
  .hero-title{position:absolute;left:58px;top:52px;font-size:36px;font-style:italic;color:var(--green);font-weight:400}
  .hero-lead{position:absolute;left:58px;top:90px;width:400px;font-size:19px;line-height:23px}
  .options{margin-top:14px}
  .logo{position:absolute;left:642px;top:700px;display:flex;align-items:center;gap:8px}
  .logo-mark{width:42px;height:42px;background:var(--ink)}
  .logo-name{font-family:"Arimo",Arial,sans-serif;font-weight:700;font-size:16px;line-height:19px;color:var(--ink)}
</style>
</head>
<body>
<main class="brochure">
  <svg class="waves" viewBox="0 0 1200 776" aria-hidden="true">
    <path d="M0,598 C220,610 420,650 610,700 L610,776 L0,776 Z" fill="var(--green)"/>
    <path d="M0,618 C230,628 430,670 610,720 C640,735 660,760 680,776 L0,776 Z" fill="var(--blue)"/>
    <path d="M600,650 C800,610 1000,600 1200,595 L1200,776 L800,776 C860,720 880,680 600,650 Z" fill="var(--green)"/>
    <path d="M590,675 C820,640 1000,632 1200,628 L1200,776 L860,776 C880,730 800,690 590,675 Z" fill="var(--blue)"/>
    <path d="M600,700 C700,685 820,690 850,776 L640,776 Z" fill="var(--white)"/>
  </svg>

  <div class="photo photo--crawling-baby" role="img" aria-label="Photo of a smiling baby crawling in a light blue outfit"></div>
  <div class="photo photo--mother-baby" role="img" aria-label="Photo of a smiling mother holding her baby"></div>
  <div class="photo photo--clinician" role="img" aria-label="Photo of a smiling clinician in a white coat with arms crossed"></div>

  <h1 class="hero-title">Oh Baby!</h1>
  <p class="hero-lead">Saint Amory's offers comprehensive health advice to keep your little ones well — from birth and beyond.</p>

  <section class="block" style="left:58px;top:192px;width:225px">
    <h2>Childbirth Preparation<br>‘All About Birth’</h2>
    <p>During All About Birth, we will help you prepare for what you might expect during your labor, birth and postpartum. Our class combines interaction with our knowledgeable childbirth educators and online resources for your continued learning. Options for participating include:</p>
    <p class="options">Two evening classes<br>One half day Saturday class<br>Online course (note this course is taken at your convenience and does not include class time with our childbirth educators)</p>
  </section>

  <section class="block" style="left:54px;top:458px;width:190px">
    <h2>Breastfeeding</h2>
    <p>Get the basics you need for successful breastfeeding. This class includes techniques and tips to get you off to a good start and ideas to help fit breastfeeding into your lifestyle. Birth partners and other family members are encouraged to attend.</p>
  </section>

  <section class="block" style="left:311px;top:224px;width:220px">
    <h2 style="line-height:19px">Breastfeeding Support:<br>Mom2Mom</h2>
    <p>Join other mothers and their babies to share experiences, get encouragement, and learn ideas from experienced lactation consultants.</p>
  </section>

  <section class="block" style="left:311px;top:346px;width:245px">
    <h2>Newborn Care</h2>
    <p>Get the latest information on baby care basics, safety, early brain development and common new parent concerns in this interactive class</p>
  </section>

  <section class="block" style="left:642px;top:62px;width:215px">
    <h2>CPR-Infant-Child</h2>
    <p>From birth to age 8, learn the basic life support (BLS) skills according to National Heart Council (NHC) guidelines.</p>
  </section>

  <section class="block" style="left:642px;top:172px;width:220px">
    <h2>Infant Child First Aid:</h2>
    <p>What to Do in an Emergency<br>This course will discuss prevention and how to avoid medical emergencies included will be hands-on first aid stations with real life scenarios for practice so that you will know what to do in an emergency.</p>
  </section>

  <section class="block" style="left:642px;top:330px;width:225px">
    <h2>Sitter Ready</h2>
    <p>Sitter Ready Basic is a medically accurate, hands-on, class that teaches boys and girls ages 11–13 how to handle emergencies when caring for children. This class teaches safe and nurturing child care techniques, behavior management skills and appropriate response to medical emergencies</p>
  </section>

  <section class="block" style="left:642px;top:497px;width:215px">
    <h2>Child Passenger Safety</h2>
    <p>Motor vehicle crashes are the leading cause of injury-related death among children ages 4 and under. Car seat checks by a Certified Child Passenger Safety Technician are available at all of our metro locations. Call to schedule an appointment.</p>
  </section>

  <section class="block" style="left:873px;top:42px;width:200px">
    <h2>Siblings for Life</h2>
    <p>This fun and interactive class emphasizes the role of the older sibling and helps prepare them to welcome their new brother or sister. For children ages 3-9.</p>
  </section>

  <section class="block" style="left:873px;top:169px;width:200px">
    <h2>Baby Sing and Sign</h2>
    <p>Learn to communicate with your baby through song and signs in four simple sessions. The class is recommended for babies and toddlers 6 to 18 months.</p>
  </section>

  <section class="block" style="left:873px;top:295px;width:245px">
    <h2 style="line-height:24px">Water Works!<br>Aqua Mom Fitness</h2>
    <p>Expecting moms and new moms:<br>Water Works! Get a low-impact, lowintensity aqua workout to increase your energy and reduce fatigue. (Prenatal doctor’s release required).</p>
  </section>

  <section class="block" style="left:873px;top:446px;width:215px">
    <h2>Parent &amp; Tot Aqua</h2>
    <p>Explore the water as a safe and fun environment for you and your child. In-water participation is required of a guardian or parent. Water activities progress based on individual readiness.<br>Pre-registration is required. For children</p>
  </section>

  <div class="logo">
    <span class="logo-mark"></span>
    <span class="logo-name">Saint Amory's<br>Women's Services</span>
  </div>
</main>
</body>
</html>
```